Business Card Design

we specialise in supply of custom uniforms - teamwear to Schools and sporting clubs, see our website: www.harbourkitcove.com.au, our main corporate colour is black and white, with small amount of gold/yellow

Industry/Entity Type

Business

Contact Information for Business Card

Harbour Kit Cove
Travis Okafor
Ph 03 6218 5097
Mobile 0462 318 740
email: travis@harbourkitcove.com.au
www.harbourkitcove.com.au
like us on facebook

Requirements
Must have
• modern look & feel

```html
<!DOCTYPE html>
<html lang="en">
<head>
<meta charset="utf-8">
<title>Harbour Kit Cove – Business Card</title>
<link rel="stylesheet" href="https://fonts.googleapis.com/css2?family=Barlow+Condensed:wght@400;700&display=swap">
<style>
  :root {
    --backdrop: #e9e7e2;
    --card-black: #111111;
    --card-yellow: #f7e100;
    --band-grey: #6e6e6e;
    --ink-white: #ffffff;
    --ink-dark: #1a1a1a;
  }
  html, body {
    margin: 0;
    padding: 0;
    width: 1200px;
    height: 1023px;
    overflow: hidden;
    background: var(--backdrop);
  }
  .canvas {
    position: relative;
    width: 1200px;
    height: 1023px;
  }
  .business-card {
    position: absolute;
    left: 100px;
    top: 226px;
    width: 1000px;
    height: 572px;
    background: var(--card-yellow);
    overflow: hidden;
    box-shadow: 0 12px 30px rgba(0,0,0,0.25);
    font-family: "Barlow Condensed", "Arial Narrow", sans-serif;
  }
  .card-shapes {
    position: absolute;
    inset: 0;
  }
  .brand-name {
    position: absolute;
    left: 520px;
    top: 118px;
    display: flex;
    align-items: center;
    gap: 16px;
    color: var(--ink-white);
    font-weight: 700;
    font-size: 50px;
    line-height: 1;
    margin: 0;
  }
  .brand-dot {
    width: 26px;
    height: 26px;
    border-radius: 50%;
    background: var(--ink-white);
  }
  .holder {
    position: absolute;
    right: 60px;
    top: 440px;
    text-align: right;
    color: var(--ink-dark);
  }
  .holder-name {
    margin: 0;
    font-weight: 700;
    font-size: 38px;
    line-height: 1.05;
  }
  .holder-role {
    margin: 2px 0 0;
    font-weight: 400;
    font-size: 24px;
  }
  .contact-list {
    position: absolute;
    left: 90px;
    top: 428px;
    margin: 0;
    padding: 0;
    list-style: none;
    color: var(--ink-dark);
    font-size: 22px;
    line-height: 30px;
  }
  .contact-item {
    display: flex;
    align-items: center;
    gap: 14px;
  }
  .contact-icon {
    width: 18px;
    height: 18px;
    fill: var(--ink-dark);
    flex: none;
  }
</style>
</head>
<body>
<main class="canvas">
  <article class="business-card">
    <svg class="card-shapes" viewBox="0 0 1000 572" width="1000" height="572" aria-hidden="true">
      <path class="grey-band" fill="var(--band-grey)" d="M0,0 L1000,0 L1000,416 C500,346 80,216 0,31 Z"/>
      <path class="black-field" fill="var(--card-black)" d="M0,0 L1000,0 L1000,400 C500,330 80,200 0,15 Z"/>
    </svg>

    <h1 class="brand-name"><span class="brand-dot"></span>Harbour Kit Cove</h1>

    <div class="holder">
      <p class="holder-name">Travis Okafor</p>
      <p class="holder-role">Owner / Proprietor</p>
    </div>

    <ul class="contact-list">
      <li class="contact-item">
        <svg class="contact-icon" viewBox="0 0 20 20"><path d="M3 4c0-1 1-2 2-2h10c1 0 2 1 2 2v2h-4V4H7v2H3z M4 8h12l1 9H3z"/></svg>
        03 6218 5097
      </li>
      <li class="contact-item">
        <svg class="contact-icon" viewBox="0 0 20 20"><path d="M6 1h8c1 0 2 1 2 2v14c0 1-1 2-2 2H6c-1 0-2-1-2-2V3c0-1 1-2 2-2zm0 3v11h8V4z"/></svg>
        0462 318 740
      </li>
      <li class="contact-item">
        <svg class="contact-icon" viewBox="0 0 20 20"><circle cx="10" cy="10" r="8" fill="none" stroke="#1a1a1a" stroke-width="2"/><path d="M2 10h16M10 2c-4 4-4 12 0 16M10 2c4 4 4 12 0 16" fill="none" stroke="#1a1a1a" stroke-width="1.5"/></svg>
        www.harbourkitcove.com.au
      </li>
      <li class="contact-item">
        <svg class="contact-icon" viewBox="0 0 20 20"><path d="M1 4h18v12H1z M2 5l8 6 8-6" fill="#1a1a1a" stroke="#f7e100" stroke-width="1.2"/></svg>
        travis@harbourkitcove.com.au
      </li>
    </ul>
  </article>
</main>
</body>
</html>
```